Ridgewell Stonecraft Construction Needs business card

Hey we are in need of business card designs. I have upload our logo as a guideline, but free feel to run with it or come up with something unique.
Pls have fun with it and be creative. the name says it all!
i will give some directions after i see a few entries..
Logo source file has been uploaded..
Hey because of the logo is so colourful already.
Can we have a few submissions with less colour.
Also we are looking for clever/hidden/descriptive business card.

```html
<!DOCTYPE html>
<html lang="en">
<head>
<meta charset="utf-8">
<title>Ridgewell Stonecraft Construction – Business Cards</title>
<link rel="stylesheet" href="https://fonts.googleapis.com/css2?family=Arimo:wght@400;700&display=swap">
<style>
  :root {
    --stage: #d9d9d9;
    --card-dark: #050505;
    --card-light: #ffffff;
    --ink-white: #ffffff;
    --ink-grey: #8a8a8a;
    --ink-dark: #1a1a1a;
    --accent-red: #e8262b;
    --accent-blue: #1a8fd6;
    --accent-yellow: #ffcc00;
    --rule-pink: #e2a0a4;
    --icon-blue: #2a9ad8;
  }
  * { box-sizing: border-box; margin: 0; padding: 0; }
  html, body { width: 1200px; height: 960px; overflow: hidden; }
  body {
    background: var(--stage);
    font-family: "Arimo", Arial, sans-serif;
    position: relative;
  }

  /* Front card (dark, vertical) */
  .card-front {
    position: absolute;
    left: 120px; top: 170px;
    width: 340px; height: 595px;
    background: var(--card-dark);
    color: var(--ink-white);
  }
  .card-front .brand {
    position: absolute;
    left: 0; right: 0; top: 220px;
    text-align: center;
  }
  .brand-mark {
    display: block;
    width: 22px; height: 22px;
    margin: 0 auto 14px;
    background: var(--accent-red);
  }
  .brand-name {
    font-weight: 700;
    font-size: 26px;
    letter-spacing: 0.5px;
    line-height: 1.15;
    text-transform: uppercase;
  }
  .card-front .brand-name { color: var(--ink-white); }
  .card-front .divider {
    position: absolute;
    left: 0; right: 0; top: 400px;
    height: 1px;
    background: var(--accent-red);
  }
  .card-front .website {
    position: absolute;
    left: 0; right: 0; top: 418px;
    text-align: center;
    font-size: 13px;
    letter-spacing: 0.3px;
  }

  /* Back card (white, horizontal) */
  .card-back {
    position: absolute;
    left: 540px; top: 390px;
    width: 620px; height: 354px;
    background: var(--card-light);
    color: var(--ink-dark);
  }
  .card-back .brand {
    position: absolute;
    left: 230px; width: 330px; top: 34px;
    text-align: center;
  }
  .card-back .brand-name { color: var(--ink-grey); font-size: 28px; }
  .name-rule {
    position: absolute;
    left: 0; right: 0; top: 176px;
    height: 3px;
    background: var(--accent-red);
  }
  .person {
    position: absolute;
    left: 350px; top: 166px;
    padding: 0 12px;
    background: var(--card-light);
    text-align: center;
  }
  .person-name {
    font-size: 15px;
    letter-spacing: 0.5px;
    text-transform: uppercase;
  }
  .person-name .first { color: var(--accent-red); }
  .person-name .last { color: var(--accent-blue); }
  .person-role {
    margin-top: 3px;
    font-size: 10px;
    color: var(--ink-grey);
    text-transform: uppercase;
    letter-spacing: 0.3px;
  }
  .contact-list {
    position: absolute;
    left: 18px; top: 210px;
    padding-left: 10px;
    border-left: 3px solid var(--rule-pink);
    list-style: none;
  }
  .contact-list li {
    display: flex;
    align-items: center;
    gap: 10px;
    height: 26px;
    font-size: 14px;
  }
  .contact-list svg { width: 18px; height: 18px; fill: var(--icon-blue); }
  .footer-rule {
    position: absolute;
    left: 0; right: 0; bottom: 26px;
    height: 3px;
    background: var(--rule-pink);
  }
  .footer-band {
    position: absolute;
    left: 0; right: 0; bottom: 0;
    height: 22px;
    background: var(--accent-yellow);
  }
</style>
</head>
<body>

  <section class="card-front">
    <div class="brand">
      <span class="brand-mark"></span>
      <p class="brand-name">Ridgewell Stonecraft<br>Construction</p>
    </div>
    <div class="divider"></div>
    <p class="website">www.ridgewellstonecraft.com</p>
  </section>

  <section class="card-back">
    <div class="brand">
      <span class="brand-mark"></span>
      <p class="brand-name">Ridgewell Stonecraft<br>Construction</p>
    </div>

    <div class="name-rule"></div>
    <div class="person">
      <p class="person-name"><span class="first">Name</span> <span class="last">Surname</span></p>
      <p class="person-role">Designation</p>
    </div>

    <ul class="contact-list">
      <li>
        <svg viewBox="0 0 24 24" aria-hidden="true"><path d="M6.6 10.8a15 15 0 0 0 6.6 6.6l2.2-2.2c.3-.3.7-.4 1-.2 1.1.4 2.3.6 3.6.6.6 0 1 .4 1 1V20c0 .6-.4 1-1 1A17 17 0 0 1 3 4c0-.6.4-1 1-1h3.5c.6 0 1 .4 1 1 0 1.3.2 2.5.6 3.6.1.3 0 .7-.2 1z"/></svg>
        <span>55 555 55555</span>
      </li>
      <li>
        <svg viewBox="0 0 24 24" aria-hidden="true"><path d="M2 5h20v14H2z M4 7v.5l8 5 8-5V7l-8 5z" fill-rule="evenodd"/></svg>
        <span>info@ridgewellstonecraft.com</span>
      </li>
      <li>
        <svg viewBox="0 0 24 24" aria-hidden="true"><path d="M12 2a7 7 0 0 0-7 7c0 5 7 13 7 13s7-8 7-13a7 7 0 0 0-7-7zm0 9.5A2.5 2.5 0 1 1 12 6.5a2.5 2.5 0 0 1 0 5z"/></svg>
        <span>area code ,no , state zip</span>
      </li>
      <li>
        <svg viewBox="0 0 24 24" aria-hidden="true"><path d="M12 2a10 10 0 1 0 0 20 10 10 0 0 0 0-20zm6.9 9h-3a15 15 0 0 0-1.3-6A8 8 0 0 1 18.9 11zM12 4.1c.9 1.2 1.7 3.6 1.9 6.9h-3.8c.2-3.3 1-5.7 1.9-6.9zM9.4 5a15 15 0 0 0-1.3 6h-3A8 8 0 0 1 9.4 5zM5.1 13h3a15 15 0 0 0 1.3 6A8 8 0 0 1 5.1 13zm6.9 6.9c-.9-1.2-1.7-3.6-1.9-6.9h3.8c-.2 3.3-1 5.7-1.9 6.9zm2.6-.9a15 15 0 0 0 1.3-6h3a8 8 0 0 1-4.3 6z"/></svg>
        <span>www.ridgewellstonecraft.com</span>
      </li>
    </ul>

    <div class="footer-rule"></div>
    <div class="footer-band"></div>
  </section>

</body>
</html>
```